Crest of Morning Paddocks Business Cards with logo

Need a creative business card that pops. Colorful but professional. The attached logo should be included. We are a national horse racing partnership so we are in the equine business. Nothing cartoonlike or whimsical.

Target Market(s)

professionals - 40+

Contact Information for Business Card

Maren Dunleavy
Director of Operations
27 Ashbrook Lane
Larkhaven, VA. 22951

Phone (540) 555-0147

FX: (540) 555-0192

email: maren@cmpaddocks.example
cmpaddocks.example

Requirements
Must have
• All information above should be on the business card including the website address. Professional yet creative
Nice to have
• an attention grabbing design. not boring. exciting.
Should not have
• cartoon like - whimsical.

```html
<!DOCTYPE html>
<html lang="en">
<head>
<meta charset="UTF-8">
<title>Crest of Morning Paddocks – Business Cards</title>
<link href="https://fonts.googleapis.com/css2?family=Signika:wght@400;600&display=swap" rel="stylesheet">
<style>
  :root {
    --page-bg: #e4e4e4;
    --card-white: #ffffff;
    --royal-blue: #2c3580;
    --royal-blue-light: #3c4aa6;
    --royal-blue-dark: #262c6b;
    --gold: #c9a227;
    --ink-blue: #2b3486;
  }
  * { box-sizing: border-box; margin: 0; padding: 0; }
  html, body {
    width: 1200px;
    height: 960px;
    overflow: hidden;
    background: var(--page-bg);
    font-family: "Signika", "Helvetica Neue", Arial, sans-serif;
  }
  .sheet {
    width: 1200px;
    height: 960px;
    display: flex;
    flex-direction: column;
    align-items: center;
    justify-content: center;
    gap: 56px;
  }
  .card {
    width: 700px;
    height: 400px;
    position: relative;
    box-shadow: 0 10px 28px rgba(0, 0, 0, 0.18);
  }

  /* Front */
  .card-front {
    background: var(--card-white);
    display: flex;
    align-items: center;
  }
  .brand-mark {
    width: 200px;
    height: 200px;
    border: 2px solid var(--gold);
    border-radius: 50%;
    display: flex;
    align-items: center;
    justify-content: center;
    text-align: center;
    color: var(--ink-blue);
    font-weight: 600;
    font-size: 22px;
    line-height: 1.2;
    letter-spacing: 2px;
    text-transform: uppercase;
    padding: 0 22px;
  }
  .card-front .brand-mark { margin-left: 90px; }
  .divider {
    margin-left: 60px;
    width: 3px;
    height: 210px;
    display: flex;
    flex-direction: column;
  }
  .divider-gold { height: 34px; background: var(--gold); }
  .divider-gap { height: 14px; }
  .divider-blue { flex: 1; background: var(--royal-blue); }
  .contact {
    margin-left: 26px;
    color: var(--ink-blue);
    font-size: 17px;
    font-weight: 400;
    line-height: 1.35;
  }
  .contact-name {
    color: var(--gold);
    font-weight: 600;
    font-size: 25px;
    line-height: 1.1;
  }
  .contact-title { margin-bottom: 8px; }

  /* Back */
  .card-back {
    background: radial-gradient(ellipse at 30% 20%, var(--royal-blue-light) 0%, var(--royal-blue) 50%, var(--royal-blue-dark) 100%);
    display: flex;
    align-items: center;
    justify-content: center;
  }
  .card-back .brand-mark {
    color: var(--card-white);
    border-color: var(--gold);
  }
</style>
</head>
<body>
  <main class="sheet">
    <section class="card card-front" aria-label="Business card front">
      <div class="brand-mark">Crest of Morning Paddocks</div>
      <div class="divider" aria-hidden="true">
        <span class="divider-gold"></span>
        <span class="divider-gap"></span>
        <span class="divider-blue"></span>
      </div>
      <div class="contact">
        <p class="contact-name">Maren Dunleavy</p>
        <p class="contact-title">Director of Operations</p>
        <p>P (540) 555-0147</p>
        <p>F (540) 555-0192</p>
        <p>maren@cmpaddocks.example</p>
        <p>cmpaddocks.example</p>
        <p>27 Ashbrook Lane</p>
        <p>Larkhaven, VA. 22951</p>
      </div>
    </section>

    <section class="card card-back" aria-label="Business card back">
      <div class="brand-mark">Crest of Morning Paddocks</div>
    </section>
  </main>
</body>
</html>
```